Very Simple Web Redesign Project - Using Photoshop

Required is a very simple website home page redesign for the following site: http://www.kestrelslateworks.com.au/
I require this as a Photoshop design.
The basic look and feel of the site needs to remain.
Specifically the colours don't need to be changed.
The positioning of the site is currently correct for the target market.
The site does not need to be made super slick looking. Just upgraded to a new version.
The current text can all be used.
The only menus necessary are a horizontal menu at the top, and a simple horizontal text menu at the bottom of the page. Do NOT retain the vertical menu on the home page (having the items "Our Gallery", "Our Services", "Enquire Now").
Give the horizontal menu the following items:
Home | Slate Roof Repairs | Slate Reroofing | Slate Roof Benefits | Other Services | Photo Gallery | FAQ's | Free Quote | Contact Us
The picture of the house at the top RHS of the page needs to be reduced in size by approx 50% and moved to the top LHS of the page.
Please place the following text into the top of the page:
"Call Now: 0427 618 302"
Keep the four pictures on the home page layout. Some larger images attached.
Thanks,
Ned
Updates
Hi,
Thanks for all the designs.
I am working with my client to get which one they like the most.
Thanks,
Ned

```html
<!DOCTYPE html>
<html lang="en">
<head>
<meta charset="utf-8">
<title>Kestrel Slateworks – Home</title>
<link rel="stylesheet" href="https://fonts.googleapis.com/css2?family=Arimo:wght@400;700&display=swap">
<style>
  :root {
    --green-dark: #2f6a12;
    --green-mid: #3f8a1c;
    --green-light: #5aa52a;
    --nav-top: #4f9a22;
    --nav-bottom: #2f7410;
    --gold: #f2b705;
    --gold-menu: #d3a90c;
    --ink: #ffffff;
    --panel-top: #3a3a3a;
    --panel-bottom: #050505;
    --bar-grey: #e9e9e9;
    --ticker-text: #3d7d12;
    --stage-black: #000000;
  }
  * { box-sizing: border-box; margin: 0; padding: 0; }
  html, body { width: 1200px; height: 900px; overflow: hidden; }
  body {
    position: relative;
    background: var(--stage-black);
    font-family: "Arimo", Arial, sans-serif;
    color: var(--ink);
  }
  .page {
    position: absolute; left: 0; top: 0; width: 1200px; height: 722px;
    background:
      repeating-linear-gradient(135deg, rgba(255,255,255,0.03) 0 2px, transparent 2px 5px),
      radial-gradient(ellipse 700px 420px at 80px 40px, var(--green-light) 0 60%, transparent 61%),
      linear-gradient(180deg, var(--green-mid), #3c8a1a 60%, #4a9a22);
    overflow: hidden;
  }
  .ticker {
    position: absolute; left: 0; top: 0; width: 1200px; height: 30px;
    background: linear-gradient(180deg, #f7f7f7, var(--bar-grey));
    box-shadow: 0 2px 4px rgba(0,0,0,0.3);
  }
  .ticker-label {
    position: absolute; left: 150px; top: 0; width: 68px; height: 30px;
    background: linear-gradient(180deg, #f0c21c, #d9a400);
    font-size: 10px; font-weight: 700; line-height: 30px; text-align: center;
  }
  .ticker-text {
    position: absolute; left: 226px; top: 0; line-height: 30px;
    font-size: 9.8px; color: var(--ticker-text); white-space: nowrap;
  }
  .brand {
    position: absolute; left: 164px; font-size: 33px; letter-spacing: 0.3px; color: var(--ink);
  }
  .call {
    position: absolute; right: 164px; text-align: right; color: var(--gold); line-height: 1.15;
  }
  .call-lead { font-size: 16px; font-weight: 700; }
  .call-number { font-size: 19px; }
  .main-nav {
    position: absolute; left: 150px; width: 900px; height: 30px;
    border-radius: 14px 14px 0 0;
    background: linear-gradient(180deg, var(--nav-top), var(--nav-bottom));
    display: flex; justify-content: center; gap: 16px;
    font-size: 12px; line-height: 31px;
  }
  .main-nav span { white-space: nowrap; }
  .hero {
    position: absolute; left: 150px; width: 900px;
    background:
      linear-gradient(90deg, rgba(48,70,20,0.85) 0 9%, transparent 22% 80%, rgba(90,120,30,0.9) 95%),
      linear-gradient(180deg, #6e7580 0%, #5a5e66 45%, #8a7a6c 70%, #c8c4b8 88%, #6b6a62 100%);
  }
  .dots { position: absolute; left: 395px; top: 320px; display: flex; gap: 15px; }
  .dots i { width: 10px; height: 10px; border-radius: 50%; background: #111; display: block; }
  .dots i.active { background: var(--gold); }
  .intro {
    position: absolute; left: 150px; top: 460px; width: 900px; height: 190px;
    border-radius: 0 0 16px 16px;
    background: linear-gradient(180deg, var(--panel-top), var(--panel-bottom));
    padding: 13px 12px 13px 18px; font-size: 11.8px; line-height: 14.5px;
  }
  .intro p { margin-bottom: 14.5px; }
  .intro a { color: var(--gold); text-decoration: none; }
  .footer-note {
    position: absolute; left: 157px; top: 657px; display: flex; align-items: center; gap: 11px;
    font-size: 10px; font-weight: 700;
  }
  .footer-mark { width: 30px; height: 30px; border-radius: 50%; background: var(--green-dark); }
  .footer-nav {
    position: absolute; right: 161px; top: 666px; display: flex; gap: 10px;
    font-size: 10px; font-weight: 700; white-space: nowrap;
  }
  .menu-state {
    position: absolute; left: 150px; top: 736px; width: 900px; height: 139px;
    background:
      repeating-linear-gradient(135deg, rgba(255,255,255,0.03) 0 2px, transparent 2px 5px),
      radial-gradient(ellipse 500px 200px at 0 0, var(--green-light) 0 55%, transparent 56%),
      linear-gradient(180deg, var(--green-mid), #3a8418);
    overflow: hidden;
  }
  .dropdown {
    position: absolute; left: 606px; top: 831px; width: 101px;
    background: var(--gold-menu); font-size: 12px;
  }
  .dropdown span { display: block; height: 25.5px; line-height: 25px; padding-left: 8px; }
  .dropdown span + span { border-top: 1px solid #e6c450; }
</style>
</head>
<body>
  <div class="page">
    <div class="ticker">
      <div class="ticker-label">Welocome!</div>
      <div class="ticker-text">We service all inner city suburbs of Sydney roughly covering an area encompassing Gordon to Epping, Mosman to Bondi, Coogee to Kogarah and Kingsgrove to Burwood and Concord</div>
    </div>

    <div class="brand" style="top:41px">Kestrel Slateworks</div>
    <div class="call" style="top:44px">
      <div class="call-lead">Call Now for a free quote</div>
      <div class="call-number">0427 618 302</div>
    </div>

    <nav class="main-nav" style="top:96px">
      <span>Home</span><span>Slate Roof Repairs</span><span>Slate Reroofing</span><span>Slate Roof Benefits</span><span>Other Services</span><span>Photo Gallery</span><span>FAQ's</span><span>Free Quote</span><span>Contact Us</span>
    </nav>

    <div class="hero" style="top:125px;height:335px" role="img" aria-label="Photo of a restored slate roof with white ridge flashing and trees at the sides">
      <div class="dots"><i></i><i class="active"></i><i></i><i></i><i></i></div>
    </div>

    <section class="intro">
      <p>At Kestrel Slateworks we specialize in the upkeep, maintenance, repair and replacement of all types of slate roof as well as wood shingles.&nbsp; We can track down the leak that just won't go away or give your house a complete re-roof. We can also provide all your guttering needs.</p>
      <p>Kestrel Slateworks is a small company and as such we do not have the overheads that larger companies do.&nbsp; Quality work and attention to detail are our trademark.</p>
      <p>All photos on this website consist of work which I have personally done.&nbsp; The above photos provide at a quick glance a reasonable cross section of the type of work I do.</p>
      <p>By clicking on the <a href="#">Photo Gallery</a> link you can see other work including some before and after shots.</p>
      <p>Feel free to call at your earliest convenience to organise an obligation free quote or fill out a form by clicking on the <a href="#">Contact Us</a> link below.</p>
    </section>

    <div class="footer-note"><span class="footer-mark"></span><span>© 2009 Kestrel Slateworks</span></div>
    <nav class="footer-nav">
      <span>Home</span><span>Photo Gallery</span><span>FAQ's</span><span>Free Quote</span><span>Contact Us</span>
    </nav>
  </div>

  <div class="menu-state">
    <div class="brand" style="top:11px;left:14px">Kestrel Slateworks</div>
    <div class="call" style="top:14px;right:14px">
      <div class="call-lead">Call Now for a free quote</div>
      <div class="call-number">0427 618 302</div>
    </div>
    <nav class="main-nav" style="top:65px;left:0">
      <span>Home</span><span>Slate Roof Repairs</span><span>Slate Reroofing</span><span>Slate Roof Benefits</span><span>Other Services</span><span>Photo Gallery</span><span>FAQ's</span><span>Free Quote</span><span>Contact Us</span>
    </nav>
    <div class="hero" style="top:95px;left:0;height:44px" role="img" aria-label="Top edge of the slate roof photo"></div>
  </div>
  <div class="dropdown">
    <span>Our Services</span>
    <span>Fact File</span>
  </div>
</body>
</html>
```